Magazine site

We are replacing this site www.thebrixtonmachinist.net to almost be exactly like pinebarklumbernews.net and thebrixtonbuilder.net, except the engineer will display a blog article on the home page.
Updates

Industry/Entity Type

Engineer

Requirements
Must have
• Blog Article

```html
<!DOCTYPE html>
<html lang="en">
<head>
<meta charset="utf-8">
<title>The Brixton Machinist</title>
<link href="https://fonts.googleapis.com/css2?family=Source+Sans+3:wght@400;600;700&family=Noto+Sans:wght@400;700&family=Noto+Serif:wght@400;700&display=swap" rel="stylesheet">
<style>
:root{
  --brown:#6e2a16;
  --brown-dark:#5a2010;
  --maroon:#8a1f12;
  --page:#f7f6f1;
  --panel:#ececea;
  --strip:#cfccc4;
  --text:#3a3a3a;
  --muted:#7b7b7b;
  --link:#1a1ad0;
  --blue:#2f67a8;
}
*{box-sizing:border-box;margin:0;padding:0}
html,body{width:1200px;height:1189px;overflow:hidden}
body{position:relative;background:var(--page);font-family:"Source Sans 3",sans-serif;color:var(--text)}
.abs{position:absolute}
.masthead{left:0;top:0;width:1200px;height:123px;background:linear-gradient(#6e2a16 0,#6e2a16 85%,#8b5a46 100%)}
.brand{left:108px;top:30px;color:#f2e6dc;font-size:50px;font-weight:400;letter-spacing:-.5px}
.top-links{left:922px;top:30px;color:#f4e9e0;font-size:14px;line-height:15px;list-style:none}
.top-links li{position:relative;padding-left:18px;margin-bottom:14px}
.top-links li::before{content:"";position:absolute;left:2px;top:2px;border-left:7px solid #fff;border-top:6px solid transparent;border-bottom:6px solid transparent}
.nav-strip{left:0;top:123px;width:1200px;height:42px;background:var(--strip)}
.nav-btn{top:129px;width:94px;height:32px;background:linear-gradient(#fff,#f1f0ec);border-radius:3px;text-align:center;line-height:32px;font-size:14px;color:var(--maroon)}
.main-panel{left:73px;top:181px;width:1054px;height:705px;background:var(--panel);border-radius:6px}
.news-card{left:81px;top:189px;width:650px;height:586px;background:#fff;border-radius:6px}
.news-title{left:97px;top:210px;font-size:18px;color:var(--brown-dark);font-weight:400}
.lead-link{left:106px;top:256px;font-size:13px;color:var(--link)}
.stamp{left:106px;top:273px;font-size:11px;color:var(--muted)}
.lead-excerpt{left:106px;top:301px;width:600px;font-size:12px;color:var(--muted);line-height:15px}
.section-bar{left:92px;width:628px;height:32px;background:linear-gradient(#fbf8f8,#f2eaea);font-size:13.5px;line-height:30px;padding-left:16px;color:#333}
.headline{font-size:13.5px;color:#555}
.marker{width:0;height:0;border-left:6px solid #a3321c;border-top:6px solid transparent;border-bottom:6px solid transparent}
.search-box{left:760px;top:196px;width:342px;height:130px;background:#f5f4ef;border-radius:6px}
.search-label{left:790px;top:204px;font-size:18px;color:#333}
.search-input{left:796px;top:254px;width:223px;height:34px;background:#fff;border:1px solid #7a3a24}
.go-btn{left:1031px;top:254px;width:49px;height:30px;background:var(--brown);color:#fff;border-radius:7px;text-align:center;line-height:30px;font-size:16px}
.nl-title{left:777px;top:343px;font-family:"Noto Serif",serif;font-size:17px;color:#333;font-weight:700}
.nl-rule{left:777px;top:369px;width:308px;border-top:1px dotted #bbb}
.nl-text{left:777px;top:382px;width:300px;font-family:"Noto Sans",sans-serif;font-size:12px;line-height:15px;color:#333}
.nl-input{left:777px;top:424px;width:308px;height:34px;background:#fff;border:1px solid #ccc;border-radius:3px;font-family:"Noto Sans",sans-serif;font-size:10px;color:#bbb;padding:11px 12px;letter-spacing:.5px}
.nl-btn{left:777px;top:470px;width:170px;height:33px;background:linear-gradient(#5b8fcc,#2d64a6);border:1px solid #2b5a92;border-radius:3px;color:#fff;font-family:"Noto Serif",serif;font-size:13px;line-height:31px;padding-left:13px}
.sponsor-box{left:756px;top:551px;width:342px;height:267px;background:#e6e4df;border-radius:6px}
.sponsor-label{left:756px;top:564px;width:342px;text-align:center;font-size:13.5px;color:var(--blue)}
.ad{left:802px;top:589px;width:260px;height:205px;border:1px solid #999;background:linear-gradient(#ffffff 0%,#f3f1ee 45%,#d9d7d4 100%)}
.promo{top:788px;width:276px;height:80px;border-radius:6px;background:linear-gradient(#fff,#dcdbd8);border:1px solid #c8c6c0}
.promo-divider{left:72px;top:10px;height:60px;border-left:1px solid #c9c7c2}
.promo-title{font-size:24px;font-weight:700;color:#9b2010;line-height:30px}
.promo-sub{font-size:14px;color:#8a8a8a}
.foot-sheet{left:73px;top:886px;width:1054px;height:303px;background:#fff}
.foot-nav{left:73px;top:898px;width:1054px;height:41px;background:var(--strip)}
.foot-link{top:910px;font-size:14px;color:var(--maroon)}
.legal{font-family:"Noto Sans",sans-serif;color:#444}
</style>
</head>
<body>
<header class="abs masthead"></header>
<div class="abs brand">The Brixton Machinist</div>
<ul class="abs top-links">
  <li>Customer FTP Access</li>
  <li>Click here to have BX Machinist delivered<br>to your door!</li>
</ul>

<nav>
  <div class="abs nav-strip"></div>
  <div class="abs nav-btn" style="left:105px">Home</div>
  <div class="abs nav-btn" style="left:215px">Current issue</div>
  <div class="abs nav-btn" style="left:324px">Archives</div>
  <div class="abs nav-btn" style="left:436px">Advertise</div>
  <div class="abs nav-btn" style="left:548px">Subscribe</div>
  <div class="abs nav-btn" style="left:661px">About</div>
  <div class="abs nav-btn" style="left:773px">Contact</div>
</nav>

<div class="abs main-panel"></div>
<section class="abs news-card"></section>
<h2 class="abs news-title">Engineering News from Around the World</h2>
<div class="abs lead-link">A is for Architecture: Historic Green Bay house ages like fine wine - Lakeshore Press Journal</div>
<div class="abs stamp">59 minutes ago</div>
<p class="abs lead-excerpt">A is for Architecture: Historic Green Bay house ages like fine wineLakeshore Press JournalThe distinctive architectural mix of ...</p>

<div class="abs section-bar" style="top:357px">Engineering</div>
<div class="abs headline" style="left:122px;top:405px">Hundreds celebrate Engineering Field Day - The Valley Ledger.com</div>
<div class="abs marker" style="left:110px;top:426px"></div>
<div class="abs headline" style="left:122px;top:424px">Marlowe Engineering Lands First Contract for New Colombia Office - Coastline Herald</div>

<div class="abs section-bar" style="top:495px">Contractors</div>
<div class="abs marker" style="left:114px;top:552px"></div>
<div class="abs headline" style="left:131px;top:550px">Construction on, near I-75 at Dix-Toledo will test Downriver drivers - Riverton Daily Press</div>
<div class="abs headline" style="left:131px;top:575px">Local Construction Winners and Losers - Open Column Post (blog)</div>

<div class="abs section-bar" style="top:642px">Architecture</div>
<div class="abs marker" style="left:114px;top:700px"></div>
<div class="abs headline" style="left:136px;top:698px;color:#333">A is for Architecture: Historic Green Bay house ages like fine wine - Lakeshore Press Journal</div>
<div class="abs headline" style="left:136px;top:723px;color:#333">Major Architectural Projects Unveiled at URBEX - TradeWire (press release)</div>

<div class="abs search-box"></div>
<div class="abs search-label">Search</div>
<svg class="abs" style="left:834px;top:184px" width="68" height="62" viewBox="0 0 68 62" aria-hidden="true">
  <line x1="6" y1="56" x2="28" y2="36" stroke="#222" stroke-width="5" stroke-linecap="round"/>
  <circle cx="42" cy="22" r="17" fill="#eaf6d8" stroke="#8cc63f" stroke-width="4"/>
</svg>
<div class="abs search-input"></div>
<div class="abs go-btn">GO</div>

<div class="abs nl-title">Newsletter</div>
<div class="abs nl-rule"></div>
<p class="abs nl-text">At vero eos et accusamus et iusto odio dignissimos ducimus qui blanditiis praesentium</p>
<div class="abs nl-input">your email address</div>
<div class="abs nl-btn">Subscribe <span style="position:absolute;right:8px;font-size:10px">······→</span></div>

<div class="abs sponsor-box"></div>
<div class="abs sponsor-label">News Sponsored by:</div>
<div class="abs ad" role="img" aria-label="Sponsor advertisement banner for a precast concrete supplier"></div>

<div class="abs promo" style="left:92px">
  <svg class="abs" style="left:18px;top:20px" width="46" height="40" viewBox="0 0 46 40" aria-hidden="true">
    <path d="M2 22 L16 34 L44 4 L18 24 Z" fill="#a07d14"/>
  </svg>
  <div class="abs promo-divider"></div>
  <div class="abs promo-title" style="left:92px;top:14px">Current Issue</div>
  <div class="abs promo-sub" style="left:92px;top:44px">Write something here</div>
</div>
<div class="abs promo" style="left:407px">
  <svg class="abs" style="left:14px;top:18px" width="46" height="46" viewBox="0 0 46 46" aria-hidden="true">
    <g stroke="#8cc63f" stroke-width="4" stroke-linecap="round">
      <line x1="23" y1="3" x2="23" y2="43"/><line x1="3" y1="23" x2="43" y2="23"/>
      <line x1="9" y1="9" x2="37" y2="37"/><line x1="37" y1="9" x2="9" y2="37"/>
    </g>
    <circle cx="23" cy="23" r="5" fill="#fff"/>
  </svg>
  <div class="abs promo-divider"></div>
  <div class="abs promo-title" style="left:92px;top:10px">Highlighted<br>Stories</div>
</div>

<footer>
  <div class="abs foot-sheet"></div>
  <div class="abs foot-nav"></div>
  <div class="abs foot-link" style="left:288px">Home</div>
  <div class="abs foot-link" style="left:372px">Current issue</div>
  <div class="abs foot-link" style="left:498px">Archives</div>
  <div class="abs foot-link" style="left:606px">Advertise</div>
  <div class="abs foot-link" style="left:718px">Subscribe</div>
  <div class="abs foot-link" style="left:843px">About</div>
  <div class="abs foot-link" style="left:949px">Contact</div>
  <div class="abs legal" style="left:73px;top:953px;width:1054px;text-align:center;font-size:10.5px;font-weight:700">Copyright Information</div>
  <div class="abs legal" style="left:73px;top:978px;width:1054px;text-align:center;font-size:10.5px">©2008 TheBrixtonMachinist.net [TM], All Rights Reserved.</div>
  <div class="abs legal" style="left:117px;top:1003px;font-size:10.5px">TheBrixtonMachinist.net [TM], web site pages may contain other proprietary licenses and copyright information, the terms of which</div>
  <p class="abs legal" style="left:88px;top:1049px;width:1024px;text-align:center;font-size:9.5px;line-height:17.7px">The Brixton Machinist is published bi-monthly by k7, inc. for the Brixton Engineering Alliance and sent to members of the Brixton Society of Professional Engineers, Council of Engineering Companies of Brixton, Brixton Civil Engineers Guild and Brixton Agricultural Engineers Guild, and to the Institute of Transit Engineers; local, state, and Federal government officials and agencies; businesses and institutions. Opinions expressed by the authors are not necessarily those of the Alliance or publisher nor do they accept responsibility for errors of content or omission and, as a matter of policy, neither do they endorse products or advertisements appearing herein. Parts of this periodical may be reproduced with the written consent from the Alliance and publisher. Correspondence regarding address changes should be sent to the Alliance at the address above. Correspondence regarding advertising and editorial material should be sent to k7, inc. at the address listed above.</p>
</footer>
</body>
</html>
```